A New and modern Business Card for Tarvish Commerce Partners Ltd

New and modern Logo and Business Card Attached is the current logo/business card designCurrently the business is called "Tarvish & Co." or TCP Ltd for short. This is subject to change.This business specialises in Telecoms and Energy. We work with the major networks (QX, Z7, etc) and also offer Energy Products saving clients money off their energy bills.These are business to business services.The current design incorporates a Pheonix, indicating rebirth, starting something new.We would like to maintain the Phoenix element but a newer modern style.We love colours in the logo 3 max.The aim of this is to be ultra slick and modern. I envisage Tarvish & Co. on one side of the card with long descriptions on the other side.Side 1:TCP Ltd/Logo?Side 2:TCP Ltd/Logo/Graphic?Brogan & Co.Name:Address:Phone:Email:The design is mostly flexible but must incorporate a Phoenix.For example "Tarvish & Co." with a block phoenix behind the text...up to you.

Industry/Entity Type

Telecommunications

Contact Information for Business Card

Tarvish & Co.
Address:
Name:
Phone:
Email:

Logo Text

Tarvish & Co.

Colors
33a6d7
0792cd
acd037
9bcb3c
f78f20
fece3e

Requirements
Must have
• Phoenix
• 3/4 colours max
• Blue representing Technology (wireless)
• Green for Eco Energy
• Orange for Phoenix
• White business card background
Should not have
• phoenix must not all be red/ orange fire, we are a technology service company and the phoenix colours must represent this. Fire is not representative of our company.

```html
<!DOCTYPE html>
<html lang="en">
<head>
<meta charset="utf-8">
<title>TCP Ltd Business Card</title>
<link href="https://fonts.googleapis.com/css2?family=Rubik:wght@300;400;600&family=Montserrat:wght@600;700&display=swap" rel="stylesheet">
<style>
  :root {
    --canvas: #e5e5e5;
    --card-dark: #1c1c1c;
    --card-light: #ffffff;
    --green: #9bcb3c;
    --green-light: #acd037;
    --blue: #0792cd;
    --blue-light: #33a6d7;
    --orange: #f78f20;
    --ink: #1c1c1c;
  }
  * { margin: 0; padding: 0; box-sizing: border-box; }
  html, body { width: 1200px; height: 1200px; overflow: hidden; background: var(--canvas); }
  .canvas { position: relative; width: 1200px; height: 1200px; }
  .card {
    position: absolute; left: 212px; width: 776px; height: 475px;
    box-shadow: 4px 5px 8px rgba(0,0,0,0.45);
    overflow: hidden;
  }
  .card svg.card-shapes { position: absolute; inset: 0; }
  .card--front { top: 90px; background: var(--card-dark); }
  .card--back { top: 650px; background: var(--card-light); }

  .front-mark {
    position: absolute; left: 338px; top: 140px; width: 100px; height: 100px;
    border-radius: 50%; background: var(--orange);
  }
  .front-name {
    position: absolute; left: 0; right: 0; top: 298px; text-align: center;
    font-family: "Rubik", sans-serif; font-size: 66px; line-height: 1;
    color: var(--green-light); letter-spacing: 1px;
  }
  .front-name strong { font-weight: 600; }
  .front-name span { font-weight: 300; }

  .back-name {
    position: absolute; left: 20px; top: 183px; width: 190px; text-align: center;
    font-family: "Rubik", sans-serif; font-weight: 600; font-size: 40px;
    line-height: 1; color: #ffffff;
  }
  .details { position: absolute; right: 79px; top: 0; text-align: right; }
  .details .person-name {
    position: absolute; right: 0; top: 105px; white-space: nowrap;
    font-family: "Montserrat", sans-serif; font-weight: 700; font-size: 42px;
    color: var(--blue); line-height: 1;
  }
  .details .person-role {
    position: absolute; right: 0; top: 158px; white-space: nowrap;
    font-family: "Montserrat", sans-serif; font-weight: 700; font-size: 22px;
    color: var(--ink); line-height: 1;
  }
  .contact {
    position: absolute; right: 0; white-space: nowrap;
    font-family: "Rubik", sans-serif; font-weight: 400; font-size: 14px;
    letter-spacing: 0.5px; color: var(--ink); line-height: 1;
  }
  .contact--address { top: 224px; }
  .contact--phone { top: 273px; }
  .contact--email { top: 318px; }
  .icon { position: absolute; left: 716px; width: 20px; height: 20px; }
  .icon--pin { top: 220px; }
  .icon--phone { top: 268px; }
  .icon--mail { top: 318px; }
</style>
</head>
<body>
<div class="canvas">

  <section class="card card--front">
    <svg class="card-shapes" width="776" height="475" viewBox="0 0 776 475">
      <polyline points="54,418 54,56 720,56 720,418" fill="none" stroke="var(--green)" stroke-width="3.5"/>
      <rect x="0" y="456" width="776" height="19" fill="var(--green)"/>
      <polygon points="298,436 478,436 516,475 260,475" fill="var(--blue)"/>
    </svg>
    <div class="front-mark"></div>
    <h1 class="front-name"><strong>TCP</strong> <span>Ltd</span></h1>
  </section>

  <section class="card card--back">
    <svg class="card-shapes" width="776" height="475" viewBox="0 0 776 475">
      <defs>
        <linearGradient id="arrowFill" x1="0" y1="0" x2="1" y2="0">
          <stop offset="0" stop-color="var(--blue-light)"/>
          <stop offset="1" stop-color="var(--blue)"/>
        </linearGradient>
      </defs>
      <rect x="62" y="39" width="217" height="16" fill="var(--green)"/>
      <rect x="279" y="39" width="217" height="16" fill="var(--blue)"/>
      <rect x="496" y="39" width="217" height="16" fill="var(--green)"/>
      <rect x="62" y="419" width="217" height="16" fill="var(--green)"/>
      <rect x="279" y="419" width="217" height="16" fill="var(--blue)"/>
      <rect x="496" y="419" width="217" height="16" fill="var(--green)"/>
      <polygon points="0,99 170,99 308,237 170,375 0,375" fill="url(#arrowFill)"/>
      <polygon points="265,158 354,237 265,316 344,237" fill="var(--blue)"/>
      <polygon points="188,99 206,99 344,237 206,375 188,375 326,237" fill="var(--green)"/>
    </svg>
    <div class="back-name">TCP Ltd</div>

    <div class="details">
      <h2 class="person-name">YourName</h2>
      <p class="person-role">Position</p>
      <p class="contact contact--address">Address</p>
      <p class="contact contact--phone">123-xxx-xxxx</p>
      <p class="contact contact--email">your@email.com</p>
    </div>

    <svg class="icon icon--pin" viewBox="0 0 20 20" aria-hidden="true">
      <path d="M10 1a6.5 6.5 0 0 0-6.5 6.5C3.5 12 10 19 10 19s6.5-7 6.5-11.5A6.5 6.5 0 0 0 10 1z" fill="var(--blue)"/>
      <circle cx="10" cy="7.5" r="2.5" fill="#fff"/>
    </svg>
    <svg class="icon icon--phone" viewBox="0 0 20 20" aria-hidden="true">
      <path d="M5.5 2.5l2.5 3-1.6 2c.9 2 2.6 3.8 4.6 4.7l2-1.6 3 2.5-1.8 2.7C9 15.5 4 10.5 3 4.3z" fill="var(--blue)"/>
      <path d="M11.5 3.5a5 5 0 0 1 5 5M11.5 6.3a2.3 2.3 0 0 1 2.3 2.3" fill="none" stroke="var(--blue)" stroke-width="1.6" stroke-linecap="round"/>
    </svg>
    <svg class="icon icon--mail" viewBox="0 0 20 20" aria-hidden="true">
      <rect x="1" y="4" width="18" height="13" fill="var(--blue)"/>
      <path d="M1.5 4.5L10 11l8.5-6.5M1.5 16.5l6-5.5M18.5 16.5l-6-5.5" fill="none" stroke="#fff" stroke-width="1.3"/>
    </svg>
  </section>

</div>
</body>
</html>
```